Online-Marketing Material für Recruiting-Plattform
Zielgruppe
Recruiting-Plattform für Physiotherapeuten. Wir sind Vermittler.
Aufgabenstellung
Ich benötige ein 2er Set aus Social-Media-Templates, das wir als Basis für Recruiting-Ads nutzen können.
Variante 1: (1080 x 1350) mit jeweils 285 Pixel Safe Space oben und unten (hier keine wichtigen Elemente).
Wichtig: Es handelt sich um ein Template. Daher muss es mit verschiedenen Elementen und Fotos funktionieren.
Die Elemente werden später durch variable Inhalte gesetzt. Ziel ist es, ein möglichst flexibles Format zu schaffen,
das mit unterschiedlichen Inhalten funktioniert.
Bitte orientiere dich am Grunddesign der Website kurvalent.de
Elemente und zugehörige Beispiele sind
1. Foto in querformat | Beispiel als Download)
2. Jobtitel als Headline | (Physiotherapeut (m/w/d)
3. Subtitle | Werde Teil eines wachsenden Teams
4. Arbeitszeitmodell | Vollzeit, Teilzeit
3. Ort | Hannover
4. 3 x Highlights | 1. Betriebliche Krankenversicherung 2. Tavlix 3. Gehalt bis zu 4.500 EUR
(Die Highlight variieren thematisch, daher hier bitte nur mit thematisch-neutralen Icons arbeiten.
5. Logo des Arbeitgebers (fenko) auf weiß
Variante 2 mit Foto in hochformat

```html
<!DOCTYPE html>
<html lang="de">
<head>
<meta charset="utf-8">
<title>Stellenanzeige Physiotherapeut – fenko</title>
<link rel="stylesheet" href="https://fonts.googleapis.com/css2?family=Roboto+Slab:wght@700&family=Roboto:wght@400;500&display=swap">
<style>
  :root {
    --ink: #111111;
    --accent: #c64f78;
    --brand: #1c4a59;
    --brand-dot: #2aa7b8;
    --panel: #efefef;
    --photo-light: #f3f5f6;
    --photo-mid: #d6dcdf;
    --photo-deep: #8e9aa6;
    --photo-navy: #3a4766;
    --bg: #ffffff;
    --safe-top: 253px;
    --safe-bottom: 947px;
  }
  * { margin: 0; padding: 0; box-sizing: border-box; }
  html, body { width: 960px; height: 1200px; overflow: hidden; background: var(--bg); }
  .ad {
    position: relative;
    width: 960px;
    height: 1200px;
    overflow: hidden;
    background: var(--bg);
    font-family: "Roboto", Arial, sans-serif;
    color: var(--ink);
  }

  /* decorative background, may extend outside the safe area */
  .backdrop {
    position: absolute;
    left: 0; top: 780px;
    width: 960px; height: 420px;
    background: var(--panel);
    border-top-left-radius: 120px;
  }
  .backdrop-fade {
    position: absolute;
    left: 300px; top: 660px;
    width: 660px; height: 120px;
    background: linear-gradient(to bottom, rgba(239,239,239,0), var(--panel));
  }

  /* content block, kept inside the safe area */
  .employer {
    position: absolute;
    right: 71px; top: 262px;
    display: flex; align-items: center; gap: 10px;
    font-weight: 500;
    font-size: 46px;
    line-height: 1;
    color: var(--brand);
  }
  .employer-dot {
    width: 24px; height: 24px; border-radius: 50%;
    background: var(--brand-dot);
  }
  .gender {
    position: absolute;
    left: 52px; top: 268px;
    font-family: "Roboto Slab", Georgia, serif;
    font-weight: 700;
    font-size: 30px;
    line-height: 1;
  }
  .job-title {
    position: absolute;
    left: 50px; top: 304px;
    font-family: "Roboto Slab", Georgia, serif;
    font-weight: 700;
    font-size: 78px;
    line-height: 80px;
    letter-spacing: -0.5px;
  }
  .job-meta {
    position: absolute;
    left: 52px; top: 476px;
    width: 336px; height: 56px;
    border-radius: 28px;
    background: var(--accent);
    display: flex; align-items: center; justify-content: center;
    font-weight: 500;
    font-size: 31px;
    color: var(--ink);
  }
  .highlights {
    position: absolute;
    left: 52px; top: 552px;
    list-style: none;
  }
  .highlights li {
    display: flex; align-items: center;
    height: 38px;
    font-size: 26px;
  }
  .highlights svg { width: 28px; height: 21px; margin-right: 20px; }
  .subtitle {
    position: absolute;
    right: 71px; top: 590px;
    text-align: right;
    color: var(--accent);
    font-weight: 500;
    font-size: 30px;
    line-height: 37px;
  }
  .photo {
    position: absolute;
    left: 323px; top: 690px;
    width: 637px; height: 252px;
    border-radius: 44px 0 0 44px;
    background:
      linear-gradient(100deg, rgba(58,71,102,0) 40%, rgba(58,71,102,0.35) 62%, rgba(58,71,102,0) 80%),
      linear-gradient(180deg, var(--photo-light) 0%, var(--photo-mid) 70%, var(--photo-deep) 100%);
    box-shadow: 0 16px 36px rgba(0,0,0,0.18);
  }
  .dots {
    position: absolute;
    left: 74px; top: 818px;
    width: 34px; height: 112px;
  }
</style>
</head>
<body>
<main class="ad">
  <div class="backdrop-fade"></div>
  <div class="backdrop"></div>

  <div class="employer"><span>fenko</span><span class="employer-dot"></span></div>

  <p class="gender">(M/W/D)</p>
  <h1 class="job-title">Physio-<br>therapeut</h1>
  <div class="job-meta">Vollzeit / Hannover</div>

  <ul class="highlights">
    <li><svg viewBox="0 0 32 24"><path d="M3 12 L12 20 L29 4" fill="none" stroke="#c64f78" stroke-width="4.5" stroke-linecap="round" stroke-linejoin="round"/></svg>Betriebliche KV</li>
    <li><svg viewBox="0 0 32 24"><path d="M3 12 L12 20 L29 4" fill="none" stroke="#c64f78" stroke-width="4.5" stroke-linecap="round" stroke-linejoin="round"/></svg>Tavlix</li>
    <li><svg viewBox="0 0 32 24"><path d="M3 12 L12 20 L29 4" fill="none" stroke="#c64f78" stroke-width="4.5" stroke-linecap="round" stroke-linejoin="round"/></svg>Gehalt bis 4.500 €</li>
  </ul>

  <p class="subtitle">Werde Teil eines<br>wachsenden Teams!</p>

  <div class="photo" role="img" aria-label="Foto im Querformat: Physiotherapeutin behandelt das Bein eines liegenden Patienten auf einer Therapieliege"></div>

  <svg class="dots" viewBox="0 0 34 112" aria-hidden="true">
    <g fill="#c64f78">
      <circle cx="5" cy="5" r="5"/><circle cx="29" cy="5" r="5"/>
      <circle cx="5" cy="30" r="5"/><circle cx="29" cy="30" r="5"/>
      <circle cx="5" cy="56" r="5"/><circle cx="29" cy="56" r="5"/>
      <circle cx="5" cy="82" r="5"/><circle cx="29" cy="82" r="5"/>
      <circle cx="5" cy="107" r="5"/><circle cx="29" cy="107" r="5"/>
    </g>
  </svg>
</main>
</body>
</html>
```